Classic Minimalistic Business Card

Design a classic, minimalistic Business Card. Please find inspiration in the attached Classic Minimalistic examples. My information:
Name: Glen Ovamir
Company: Ovamir Capital
Logo: OC
Address: 1470 N Thornwick Rd, Suite 210 | Brookmere, IL 60871
Phone: 630-555-0192
Email: glenovamir@pvt.insure
Slogan: Building Strength Through Capital

Feel free to leave out any of the information above except my name.

I have selected Double-sided, but I am also open to Single-sided

Target Market(s)

22-70. income greater than 150k/year

Industry/Entity Type

Finance

Contact Information for Business Card

See Project Description

Requirements
Must have
• Ivory or "antiqued" background similar to the reference pictures

```html
<!DOCTYPE html>
<html lang="en">
<head>
<meta charset="utf-8">
<title>Ovamir Capital – Business Card</title>
<link rel="stylesheet" href="https://fonts.googleapis.com/css2?family=Cinzel:wght@400;500&family=Pinyon+Script&family=Special+Elite&display=swap">
<style>
  :root {
    --backdrop: #979c98;
    --card-ivory: #e5d8c5;
    --brand-red: #a33526;
    --brand-grey: #958c83;
    --ink: #1b1714;
  }
  * { margin: 0; padding: 0; box-sizing: border-box; }
  html, body {
    width: 1200px;
    height: 1000px;
    overflow: hidden;
    background: var(--backdrop);
  }
  .card {
    position: absolute;
    left: 245px;
    top: 296px;
    width: 711px;
    height: 409px;
    background: var(--card-ivory);
  }
  .card > * {
    position: absolute;
    left: 0;
    right: 0;
    text-align: center;
    white-space: nowrap;
    font-style: normal;
  }
  .brand-mark {
    top: 36px;
    left: 332px;
    right: auto;
    width: 46px;
    height: 46px;
  }
  .brand-name {
    top: 88px;
    font-family: "Cinzel", serif;
    font-weight: 400;
    font-size: 36px;
    line-height: 40px;
    letter-spacing: 1px;
    color: var(--brand-grey);
  }
  .brand-tagline {
    top: 130px;
    font-family: "Cinzel", serif;
    font-weight: 500;
    font-size: 14px;
    line-height: 16px;
    letter-spacing: 2.4px;
    color: var(--ink);
  }
  .holder-name {
    top: 166px;
    font-family: "Pinyon Script", cursive;
    font-weight: 400;
    font-size: 68px;
    line-height: 80px;
    color: var(--brand-red);
  }
  .holder-email {
    top: 243px;
    font-family: "Special Elite", monospace;
    font-size: 22px;
    line-height: 26px;
    letter-spacing: 1px;
    color: var(--ink);
  }
  .holder-phone {
    top: 315px;
    font-family: "Special Elite", monospace;
    font-size: 25px;
    line-height: 30px;
    letter-spacing: 1.5px;
    font-weight: 700;
    color: var(--ink);
  }
  .holder-address {
    top: 352px;
    font-family: "Cinzel", serif;
    font-size: 12px;
    line-height: 19px;
    letter-spacing: 1px;
    color: var(--ink);
  }
</style>
</head>
<body>
  <main class="card">
    <svg class="brand-mark" viewBox="0 0 46 46" aria-hidden="true">
      <circle cx="23" cy="23" r="20" fill="var(--brand-red)"/>
    </svg>
    <h1 class="brand-name">OVAMIR CAPITAL</h1>
    <p class="brand-tagline">BUILDING STRENGTH THROUGH CAPITAL</p>
    <h2 class="holder-name">Glen Ovamir</h2>
    <p class="holder-email">glenovamir@pvt.insure</p>
    <p class="holder-phone">630-555-0192</p>
    <address class="holder-address">1470 N THORNWICK RD, SUITE 210<br>BROOKMERE, IL 60871</address>
  </main>
</body>
</html>
```